Logo + Business Card Design Project

We are looking at changing our logo and reprinting business cards.

Attached is a design concept for the logo (we have no hi res files for this).

The logo needs to be able to work standalone without the tagline.

We are happy for you to use this concept or design a new one. The existing concept is quite well liked.

We would also consider not having Solutions in the logo and just have QRV Systems Pty Ltd in the body text of the card.

We have a Tag Line that needs to go on all documentation / websites etc wherever the logo appears.

Tagline: Turning IT up

Our message to clients is that we have solutions that:

QRV Systems:
Turning IT up

Turning up Revenue
Turning up Profit
Turning up Confidence

We would require the files in a High Res format for print and a scalable transparent format for web.
(We also need greyscale and monochrome files)
All source files need to be delivered with existing layers etc

A corporate guide with the logo usage and colours should be specified.

Suggestions:
The new logo has to have CMYK colours of 100 90 0 0

CMYK 100 90 0 0
RGB #21409A
Websafe #224499
Greyscale #414141

We would also need a business card layout designed.
Could be one sided or 2 sided. Will probably print matt cello 2 sides on 350gsm gloss
Updates

Industry/Entity Type

Business

Requirements
Should not have
• Lower case n in QRV.

```html
<!DOCTYPE html>
<html lang="en">
<head>
<meta charset="utf-8">
<title>QRV Systems – Business Card</title>
<link rel="stylesheet" href="https://fonts.googleapis.com/css2?family=Cardo&family=Marcellus&family=Pinyon+Script&display=swap">
<style>
  :root {
    --paper: #ffffff;
    --brand-blue: #21409a;
    --gold: #b1853a;
    --gold-deep: #9a7130;
  }
  * { margin: 0; padding: 0; box-sizing: border-box; }
  html, body {
    width: 1200px;
    height: 848px;
    overflow: hidden;
    background: var(--paper);
  }
  .card {
    position: relative;
    width: 1200px;
    height: 848px;
    background: var(--paper);
    color: var(--gold);
  }
  .brand {
    position: absolute;
    top: 82px;
    left: 0;
    width: 1160px;
    height: 200px;
    display: flex;
    align-items: center;
    justify-content: center;
    gap: 30px;
  }
  .brand-dot {
    width: 150px;
    height: 150px;
    flex: none;
  }
  .brand-text {
    display: flex;
    flex-direction: column;
    align-items: flex-start;
  }
  .brand-name {
    font-family: "Marcellus", serif;
    font-size: 84px;
    font-weight: 400;
    color: var(--brand-blue);
    letter-spacing: 2px;
    line-height: 1;
  }
  .brand-tagline {
    font-family: "Marcellus", serif;
    font-size: 30px;
    font-weight: 400;
    color: var(--gold);
    letter-spacing: 3px;
    line-height: 1;
    margin-top: 14px;
    margin-left: 4px;
  }
  .person {
    position: absolute;
    top: 356px;
    left: 0;
    width: 1160px;
    text-align: center;
  }
  .person-name {
    font-family: "Marcellus", serif;
    font-size: 57px;
    font-weight: 400;
    color: var(--gold);
    letter-spacing: 1px;
    line-height: 1;
  }
  .person-role {
    font-family: "Pinyon Script", cursive;
    font-size: 64px;
    font-weight: 400;
    color: var(--gold-deep);
    line-height: 1;
    margin-top: 4px;
    margin-left: 20px;
  }
  .contact {
    position: absolute;
    top: 532px;
    font-family: "Cardo", serif;
    font-size: 27px;
    line-height: 43.5px;
    color: var(--gold);
    list-style: none;
    white-space: nowrap;
  }
  .contact-left { left: 96px; }
  .contact-right { left: 577px; }
  .address-line2 { padding-left: 130px; }
</style>
</head>
<body>
  <main class="card">
    <header class="brand">
      <svg class="brand-dot" viewBox="0 0 150 150" aria-hidden="true">
        <circle cx="75" cy="75" r="75" fill="var(--brand-blue)"/>
      </svg>
      <div class="brand-text">
        <span class="brand-name">QRV Systems</span>
        <span class="brand-tagline">Turning IT up</span>
      </div>
    </header>

    <section class="person">
      <h1 class="person-name">Daniel Verrant</h1>
      <p class="person-role">Project Director</p>
    </section>

    <ul class="contact contact-left">
      <li>Phone: + 61 2 5550-0100</li>
      <li>Support: + 61 2 5550-0133</li>
      <li>Fax: + 61 2 5550-0101</li>
      <li>Mobile: 0491 570 156</li>
    </ul>

    <ul class="contact contact-right">
      <li>Email: daniel.verrant@qrv.com.au</li>
      <li>Web:&nbsp; www.qrv.com.au</li>
      <li>Address: 310/17 Merriden Street</li>
      <li class="address-line2">Ashbury Vale NSW&nbsp; 2071</li>
    </ul>
  </main>
</body>
</html>
```